New Business Card Design Project for Handyman Business

I would like to purchase a customized version of a design you have previously submitted - https://www.artvelloshowcase.com/design/58172046
I love this design!
I am hoping you can design something similar to this for our Handyman Business.
Attached is our logo and some graphics we have used.
Here is a link to the Google Doc with the content that needs to be included, https://files.quorvandel.net/document/d/e/4QZTR-8kPw2LmXn5Hb7rYcVt-qaaJsK3Df9TgNpU4WeR__LmcXaBvKpHsd2Qjn7wo4tzhgrVb41K85o3ttSTq/pub
Target Market(s)
Real Estate Agents, Home Owners and Property Managers
Industry/Entity Type
Construction/ Speciality Trade
Contact Information for Business Card
https://files.quorvandel.net/document/d/7QwRtYpL_zxkn4BvHnCdFs8TmKjWaEr2LUXPo6cxhg/edit?usp=sharing
Font styles to use
Other font styles liked:
- Ubuntu
Look and feel
Each slider illustrates characteristics of the customer's brand and the style your logo design should communicate.

```html
<!DOCTYPE html>
<html lang="en">
<head>
<meta charset="utf-8">
<title>Fixwright Business Card</title>
<link rel="stylesheet" href="https://fonts.googleapis.com/css2?family=Ubuntu:wght@400;500;700&display=swap">
<style>
  :root {
    --stage: #d9d9d9;
    --card: #1c1c1e;
    --blue: #1a7fd0;
    --green: #3cc24a;
    --orange: #f0652a;
    --white: #f2f2f2;
    --muted: #b9b9be;
    --rule: #5a5a5e;
  }
  * { box-sizing: border-box; margin: 0; padding: 0; }
  html, body { width: 1200px; height: 1108px; overflow: hidden; }
  body {
    background: var(--stage);
    font-family: "Ubuntu", sans-serif;
    position: relative;
  }
  .card {
    position: absolute;
    top: 194px;
    width: 420px;
    height: 720px;
    background: var(--card);
    border-radius: 26px;
    color: var(--white);
    text-align: center;
    overflow: hidden;
  }
  .card--front { left: 150px; }
  .card--back { left: 630px; }

  .brand { display: flex; align-items: center; justify-content: center; gap: 12px; }
  .brand__mark { width: 34px; height: 34px; background: var(--blue); }
  .brand__name { font-size: 58px; font-weight: 500; color: var(--green); letter-spacing: -1px; line-height: 1.1; }
  .slogan {
    color: var(--muted); font-size: 16px; font-style: normal; margin-top: 8px;
  }

  .card--front .brand-block { margin-top: 150px; }
  .person { margin-top: 50px; font-size: 34px; letter-spacing: 0.5px; }
  .person__first { color: var(--blue); font-weight: 400; }
  .person__last { color: var(--green); font-weight: 700; }
  .role { font-size: 19px; margin-top: 4px; }

  .divider-row { display: flex; align-items: center; gap: 10px; margin: 16px 40px 0; }
  .rule { flex: 1; height: 1px; background: var(--rule); }
  .rule--full { margin: 14px 40px 0; }
  .icon { width: 36px; height: 36px; border-radius: 5px; display: flex; align-items: center; justify-content: center; }
  .icon--phone { background: var(--blue); }
  .icon--mail { background: var(--green); }
  .icon--web { background: var(--orange); }

  .contact { margin-top: 14px; font-size: 19px; line-height: 1.45; }
  .contact__web-a { color: var(--blue); }
  .contact__web-b { color: var(--green); }
  .service { color: var(--blue); font-size: 20px; line-height: 1.25; margin-top: 12px; }
  .offerings { color: var(--orange); font-size: 18px; margin-top: 14px; }
  .offerings .dot { color: var(--green); }

  .pattern-field {
    position: absolute; inset: 0 0 260px 0;
    background: linear-gradient(180deg, #2a2a2d 0%, #222224 60%, var(--card) 100%);
  }
  .card--back .brand-block { position: absolute; left: 0; right: 0; top: 430px; }
  .social { display: flex; justify-content: center; gap: 12px; margin-top: 22px; }
  .social__tile { width: 38px; height: 38px; border-radius: 5px; }
  .social__tile:nth-child(odd) { background: var(--blue); }
  .social__tile:nth-child(even) { background: var(--green); }
  .hashtag { font-size: 19px; margin-top: 12px; line-height: 1.25; }
</style>
</head>
<body>

<section class="card card--front">
  <div class="brand-block">
    <div class="brand">
      <span class="brand__mark"></span>
      <span class="brand__name">fixwright</span>
    </div>
    <p class="slogan">Trusted home repair, done right</p>
  </div>

  <h1 class="person"><span class="person__first">CALVIN</span> <span class="person__last">REYES</span></h1>
  <p class="role">Owner/ Handyman</p>

  <div class="divider-row">
    <span class="rule"></span>
    <span class="icon icon--phone">
      <svg width="20" height="20" viewBox="0 0 24 24"><path d="M6.6 10.8a15 15 0 0 0 6.6 6.6l2.2-2.2a1 1 0 0 1 1-.25 11.4 11.4 0 0 0 3.6.6 1 1 0 0 1 1 1V20a1 1 0 0 1-1 1A17 17 0 0 1 3 4a1 1 0 0 1 1-1h3.5a1 1 0 0 1 1 1c0 1.25.2 2.45.6 3.6a1 1 0 0 1-.25 1z" fill="#fff"/></svg>
    </span>
    <span class="icon icon--mail">
      <svg width="22" height="16" viewBox="0 0 22 16"><rect x="1" y="1" width="20" height="14" rx="1.5" fill="none" stroke="#fff" stroke-width="1.8"/><path d="M1.5 2 11 9l9.5-7" fill="none" stroke="#fff" stroke-width="1.8"/></svg>
    </span>
    <span class="icon icon--web">
      <svg width="22" height="22" viewBox="0 0 24 24" fill="none" stroke="#fff" stroke-width="1.6"><circle cx="12" cy="12" r="9"/><ellipse cx="12" cy="12" rx="4" ry="9"/><path d="M3 12h18M4.5 7.5h15M4.5 16.5h15"/></svg>
    </span>
    <span class="rule"></span>
  </div>

  <div class="contact">
    <p>(470) 555-0182</p>
    <p>calvin@fixwright-co.com</p>
    <p><span class="contact__web-a">Fixwright-</span><span class="contact__web-b">co.com</span></p>
  </div>

  <div class="rule rule--full"></div>
  <p class="service">Commercial and Resdiential<br>Handyman</p>
  <div class="rule rule--full"></div>
  <p class="offerings">Improve <span class="dot">•</span> Repair <span class="dot">•</span> Remodel <span class="dot">•</span> Maintain</p>
</section>

<section class="card card--back">
  <div class="pattern-field" role="img" aria-label="Faint repeating pattern of the company house mark"></div>
  <div class="brand-block">
    <div class="brand">
      <span class="brand__mark"></span>
      <span class="brand__name">fixwright</span>
    </div>
    <p class="slogan">Trusted home repair, done right</p>
    <div class="social" aria-label="Social media">
      <span class="social__tile"></span>
      <span class="social__tile"></span>
      <span class="social__tile"></span>
      <span class="social__tile"></span>
    </div>
    <p class="hashtag">#FixwrightHandyman<br>Services</p>
  </div>
</section>

</body>
</html>
```